Timid Kitten Clinic Business Card Design

I need a business card designed for my cat only veterinary clinic. I will upload the logo that I would like included on the card. Please include:
Business Name: The Timid Kitten Clinic
Address: 4827 W. 39th Ln, Scottsdale, AZ 85317
Phone #: 480-555-6314
Website URL: www.timidkittenvet.example
And the Doctors Name: Marla Quint, DVM

```html
<!DOCTYPE html>
<html lang="en">
<head>
<meta charset="utf-8">
<title>The Timid Kitten Clinic – Business Card</title>
<link rel="stylesheet" href="https://fonts.googleapis.com/css2?family=Quicksand:wght@500&family=Poppins:wght@700&family=Lato:wght@400&display=swap">
<style>
  :root {
    --backdrop: #ccd1d1;
    --paper: #efefed;
    --edge: #5b1670;
    --ink: #141414;
    --name: #2b1959;
    --info: #5a5a5a;
    --paw: #9669a0;
    --mark: #1c1424;
  }
  * { margin: 0; padding: 0; box-sizing: border-box; }
  html, body {
    width: 1200px; height: 929px; overflow: hidden;
    background: var(--backdrop);
  }
  .sheet {
    position: relative; width: 1200px; height: 929px;
    display: flex; align-items: center; justify-content: center; gap: 50px;
  }
  .card {
    position: relative; width: 525px; height: 300px;
    background: var(--paper);
    border-bottom: 5px solid var(--edge);
    box-shadow: 0 14px 30px rgba(0,0,0,0.18);
    overflow: hidden;
  }
  .clinic-name {
    font-family: "Quicksand", sans-serif; font-weight: 500;
    color: var(--ink); line-height: 0.98; letter-spacing: 2px;
  }
  .front .clinic-name {
    position: absolute; left: 30px; top: 26px; font-size: 40px;
  }
  .doctor {
    position: absolute; left: 30px; top: 128px;
    font-family: "Poppins", sans-serif; font-weight: 700;
    font-size: 25px; color: var(--name);
  }
  .doctor .title { font-size: 13px; }
  .contact {
    position: absolute; left: 30px; top: 170px;
    font-family: "Lato", sans-serif; color: var(--info);
    font-size: 13px; line-height: 1.45;
  }
  .contact .phone { font-size: 17px; line-height: 1.35; }
  .paw-art {
    position: absolute; right: 22px; bottom: 14px;
    width: 210px; height: 210px;
  }
  .back .lockup {
    position: absolute; left: 110px; top: 92px;
    display: flex; align-items: flex-end; gap: 0;
  }
  .logo-circle {
    width: 104px; height: 104px; border-radius: 50%;
    background: var(--mark); flex: none;
  }
  .back .clinic-name {
    font-size: 32px; margin-left: -6px; margin-bottom: -22px;
  }
</style>
</head>
<body>
<main class="sheet">
  <section class="card front">
    <h1 class="clinic-name">The Timid<br>Kitten Clinic</h1>
    <p class="doctor">Marla Quint, <span class="title">DVM</span></p>
    <address class="contact">
      4827 W. 39th Ln<br>
      Scottsdale, AZ 85317<br>
      <span class="phone">P.480-555-6314</span><br>
      www.timidkittenvet.example
    </address>
    <svg class="paw-art" viewBox="0 0 210 210" role="img" aria-label="Large purple paw print illustration">
      <rect x="0" y="0" width="210" height="210" rx="60" fill="var(--paw)"/>
    </svg>
  </section>

  <section class="card back">
    <div class="lockup">
      <div class="logo-circle" aria-hidden="true"></div>
      <h2 class="clinic-name">The Timid<br>Kitten Clinic</h2>
    </div>
  </section>
</main>
</body>
</html>
```